rk ironcraft business card metallic look

revamp the existing design but want card to have a metalic look to it

Target Market(s)

construction industry

Industry/Entity Type

constrction

Contact Information for Business Card

front of card RK Ironcraft, phone 4165550193, email rk.ironcraftt@veltrano.com and instagram account; rk_ironcraft_

Font styles to use
Other font styles liked:
• masculine

Colors

Designer to choose only greyscale colors for use in the design.

Requirements
Must have
• back side RK Ironcraft then a list of everything : Siding, ACM Panels, Standing Seam,Soffit, Fascia, Gutters,Metal,Alu,inum, Viynyl, Metal Roofs and roof repairs
Nice to have
• I would like to keep the look of the existing card with the metal grids on the front
Should not have
• Need a design in two days

```html
<!DOCTYPE html>
<html lang="en">
<head>
<meta charset="utf-8">
<title>RK Ironcraft – Business Card</title>
<link rel="stylesheet" href="https://fonts.googleapis.com/css2?family=Poppins:wght@500;600;800&display=swap">
<style>
  :root {
    --canvas: #2a2a2a;
    --card-front: #0b0b0b;
    --grid-dark: #141414;
    --grid-mid: #2c2c2c;
    --back-light: #5a5a5a;
    --back-dark: #2f2f2f;
    --brand-steel: #8c8c8c;
    --text-light: #f2f2f2;
    --text-soft: #d6d6d6;
  }
  * { box-sizing: border-box; margin: 0; padding: 0; }
  html, body {
    width: 1200px; height: 800px; overflow: hidden;
    background: var(--canvas);
    font-family: "Poppins", sans-serif;
  }
  .stage {
    width: 1200px; height: 800px;
    display: flex; flex-direction: column;
    align-items: center; justify-content: center; gap: 40px;
  }
  .card {
    width: 560px; height: 320px;
    border-radius: 4px; position: relative; overflow: hidden;
    box-shadow: 0 10px 30px rgba(0,0,0,.45);
  }

  /* Front */
  .card--front { background: var(--card-front); }
  .front__grid {
    position: absolute; inset: 0 0 40% 0;
    background: linear-gradient(180deg, var(--grid-mid) 0%, var(--grid-dark) 60%, var(--card-front) 100%);
  }
  .front__content {
    position: absolute; inset: 0;
    display: flex; flex-direction: column; align-items: center;
    padding-top: 70px;
  }
  .brand-name {
    font-weight: 800; color: var(--brand-steel);
    text-transform: uppercase; letter-spacing: 2px; line-height: 1;
  }
  .card--front .brand-name { font-size: 48px; }
  .contact-row {
    display: flex; gap: 40px; margin-top: 30px;
    font-size: 17px; font-weight: 600; color: var(--text-light);
    align-items: center;
  }
  .contact-item { display: flex; align-items: center; gap: 8px; }
  .contact-item svg { width: 18px; height: 18px; }
  .social-mark {
    width: 14px; height: 14px; border: 2px solid var(--text-soft); border-radius: 50%;
  }
  .contact-email {
    position: absolute; left: 26px; bottom: 22px;
    font-size: 15px; font-weight: 500; color: var(--text-soft);
  }

  /* Back */
  .card--back {
    background: radial-gradient(ellipse at 40% 20%, var(--back-light) 0%, var(--back-dark) 75%);
    display: flex; flex-direction: column; align-items: center; justify-content: center;
    padding: 0 40px;
  }
  .card--back .brand-name { font-size: 40px; margin-bottom: 30px; }
  .services {
    text-align: center; font-size: 16px; font-weight: 600;
    color: var(--text-light); line-height: 1.6;
  }
</style>
</head>
<body>
<main class="stage">
  <section class="card card--front">
    <div class="front__grid" role="img" aria-label="Perforated metal grid texture"></div>
    <div class="front__content">
      <div class="brand-name">RK Ironcraft</div>
      <div class="contact-row">
        <span class="contact-item">
          <svg viewBox="0 0 24 24" fill="var(--text-soft)"><path d="M6.6 10.8a15.1 15.1 0 0 0 6.6 6.6l2.2-2.2a1 1 0 0 1 1-.25 11.4 11.4 0 0 0 3.6.57 1 1 0 0 1 1 1V20a1 1 0 0 1-1 1A17 17 0 0 1 3 4a1 1 0 0 1 1-1h3.5a1 1 0 0 1 1 1c0 1.25.2 2.45.57 3.57a1 1 0 0 1-.25 1z"/></svg>
          416-555-0193
        </span>
        <span class="contact-item"><span class="social-mark"></span>rk_ironcraft_</span>
      </div>
    </div>
    <div class="contact-email contact-item">
      <svg viewBox="0 0 24 24" fill="none" stroke="var(--text-soft)" stroke-width="2"><rect x="3" y="5" width="18" height="14" rx="1"/><path d="M3 6l9 7 9-7"/></svg>
      rk.ironcraftt@veltrano.com
    </div>
  </section>

  <section class="card card--back">
    <div class="brand-name">RK Ironcraft</div>
    <p class="services">
      Siding • ACM Panels • Standing Seam • Soffit • Fascia<br>
      Gutters • Metal • Alu • inum • Viynyl • Metal Roofs<br>
      and roof repairs
    </p>
  </section>
</main>
</body>
</html>
```